Packaging Design for Dalvoren

Mission: design the layout of plastic bag
Objective: To provide advertising clients samples of commercial enterprise sector Bakery and Confectionery industry.
Information: company logo, address bar and the text:
The ingredients for the baking and confectionery industry
Advanced European technology, equipment and tools
Technological support, advice, training,
Quality guaranteed by leading European manufacturers
The company logo consist of word DALVOREN
The shape of the package: WxH 460h540, handle as punching 165?27 mm oval rounded
Preferred background color (material): Yellow
Logo color: Brown (Chocolate)
Chromaticity of printing: 1-2 colors

Design should be completed in vector format AI

```html
<!DOCTYPE html>
<html lang="en">
<head>
<meta charset="utf-8">
<title>Dalvoren — Carrier Bag</title>
<link rel="stylesheet" href="https://fonts.googleapis.com/css2?family=Arimo:wght@400;700&display=swap">
<style>
  :root {
    --yellow-deep: #ffd62e;
    --yellow-mid: #ffe77a;
    --yellow-light: #fff6c8;
    --chocolate: #6f3a2f;
    --text-yellow: #f9d33c;
    --white: #ffffff;
  }
  html, body {
    margin: 0;
    padding: 0;
    width: 969px;
    height: 1200px;
    overflow: hidden;
    background: var(--white);
  }
  .bag {
    position: relative;
    width: 969px;
    height: 1200px;
    overflow: hidden;
    background: radial-gradient(ellipse 70% 55% at 50% 62%, var(--yellow-light) 0%, var(--yellow-mid) 45%, var(--yellow-deep) 100%);
  }
  .bag__glow {
    position: absolute;
    left: 110px;
    top: 40px;
    width: 750px;
    height: 780px;
    border-radius: 50%;
    background: radial-gradient(ellipse at 50% 55%, rgba(255,250,220,0.55) 0%, rgba(255,240,170,0.25) 50%, rgba(255,230,120,0) 75%);
  }
  .bag__handle {
    position: absolute;
    left: 310px;
    top: 87px;
    width: 346px;
    height: 54px;
    border-radius: 27px;
    background: var(--white);
  }
  .brand {
    position: absolute;
    left: 0;
    right: 0;
    top: 450px;
    margin: 0;
    text-align: center;
    font-family: "Arimo", sans-serif;
    font-weight: 700;
    font-size: 120px;
    line-height: 1;
    letter-spacing: 4px;
    color: var(--chocolate);
  }
  .bag__base {
    position: absolute;
    left: 0;
    top: 640px;
    width: 969px;
    height: 560px;
  }
  .bag__base path { fill: var(--chocolate); }
  .services {
    position: absolute;
    left: 37px;
    top: 894px;
    margin: 0;
    padding: 0;
    list-style: none;
    font-family: "Arimo", sans-serif;
    font-weight: 700;
    font-size: 30px;
    line-height: 50px;
    letter-spacing: 1.5px;
    color: var(--text-yellow);
    white-space: nowrap;
  }
  .quality {
    position: absolute;
    left: 37px;
    top: 1088px;
    display: flex;
    align-items: center;
    gap: 16px;
    margin: 0;
    font-family: "Arimo", sans-serif;
    font-size: 32px;
    line-height: 44px;
    letter-spacing: 1.3px;
    color: var(--white);
    white-space: nowrap;
  }
  .quality__dot {
    width: 40px;
    height: 40px;
    border-radius: 50%;
    background: var(--text-yellow);
    flex: none;
  }
</style>
</head>
<body>
  <main class="bag">
    <div class="bag__glow" role="img" aria-label="Soft pale leaf-shaped glow behind the brand name"></div>
    <div class="bag__handle" aria-hidden="true"></div>

    <h1 class="brand">DALVOREN</h1>

    <svg class="bag__base" viewBox="0 0 969 560" aria-hidden="true">
      <path d="M0 20 Q484 406 969 20 L969 560 L0 560 Z"/>
    </svg>

    <ul class="services">
      <li>The ingredients for the baking and confectionery industry</li>
      <li>Advanced European tehnology, equipment and tools</li>
      <li>Tehnological support, advice, training</li>
    </ul>

    <p class="quality"><span class="quality__dot" aria-hidden="true"></span>Quality guarnteed by leading European manufactures</p>
  </main>
</body>
</html>
```